Prayer Service 12.28.2013

I need a flyer designed for a Christian prayer service. The title and theme is:
"Total and Complete Surrender for Total and Complete Deliverance!"
1. You have creative freedom with imagery and typography
2. I need a quick turnaround time
FLYER DETAILS:
A prayer, anointing, and deliverance all night prayer service, at Brookhaven Assembly.
Saturday December 28 2013 from 9pm-6am.
Special guest speakers, prayer,anointing,and deliverance sessions.
For more information contact Sis Mirela Thornbury at Brookhaven Assembly 347 562 1094 Ext. 4816 or Janelle Corbin at 631 538-2904

```html
<!DOCTYPE html>
<html lang="en">
<head>
<meta charset="utf-8">
<title>Total and Complete Surrender – All Night Prayer Service</title>
<link rel="stylesheet" href="https://fonts.googleapis.com/css2?family=Inter:ital,wght@0,300;0,400;0,700;0,800;1,300&display=swap">
<style>
  :root {
    --ink-black: #000000;
    --sky-slate: #5c5e66;
    --sky-dusk: #8a7e80;
    --sun-glow: #fff6ee;
    --sun-warm: #e9c2b3;
    --field-dark: #2a2a22;
    --badge-fill: rgba(70, 70, 72, 0.82);
    --text-white: #ffffff;
  }
  html, body {
    margin: 0;
    padding: 0;
    width: 834px;
    height: 1200px;
    overflow: hidden;
    background: var(--ink-black);
  }
  .flyer {
    position: relative;
    width: 834px;
    height: 1200px;
    overflow: hidden;
    font-family: "Inter", "Helvetica Neue", Arial, sans-serif;
    color: var(--text-white);
  }
  .scene {
    position: absolute;
    inset: 0;
    background:
      radial-gradient(circle at 578px 605px, var(--sun-glow) 0, var(--sun-warm) 40px, rgba(200,150,140,0.55) 120px, rgba(140,120,125,0) 320px),
      linear-gradient(180deg, var(--ink-black) 0, var(--ink-black) 190px, #3d3e44 250px, var(--sky-slate) 420px, var(--sky-dusk) 640px, #5a5450 900px, var(--field-dark) 1030px, #1c1c16 1200px);
  }
  .title {
    position: absolute;
    top: 100px;
    left: 0;
    width: 834px;
    margin: 0;
    text-align: center;
    font-weight: 700;
    font-size: 60px;
    line-height: 72px;
    letter-spacing: 0.2px;
  }
  .summary {
    position: absolute;
    top: 347px;
    left: 298px;
    width: 500px;
    margin: 0;
    font-weight: 700;
    font-size: 22.5px;
    line-height: 30px;
  }
  .date-badge {
    position: absolute;
    left: 335px;
    top: 642px;
    width: 362px;
    height: 362px;
    box-sizing: border-box;
    border: 9px solid var(--text-white);
    border-radius: 50%;
    background: var(--badge-fill);
    text-align: center;
    padding-top: 60px;
  }
  .date-day {
    display: block;
    font-weight: 700;
    font-size: 45px;
    line-height: 46px;
  }
  .date-full {
    display: block;
    font-weight: 700;
    font-size: 21px;
    line-height: 26px;
  }
  .date-time {
    display: block;
    font-weight: 700;
    font-size: 32px;
    line-height: 42px;
    margin-top: 2px;
  }
  .date-program {
    display: block;
    font-weight: 300;
    font-style: italic;
    font-size: 25px;
    line-height: 31px;
    margin-top: 2px;
  }
  .contact {
    position: absolute;
    top: 1066px;
    left: 277px;
    width: 540px;
    margin: 0;
    font-weight: 400;
    font-size: 20px;
    line-height: 27px;
  }
</style>
</head>
<body>
  <main class="flyer">
    <div class="scene" role="img" aria-label="Photograph of a man kneeling in a grassy field with hands folded in prayer, facing a sunset sky with rays breaking through clouds"></div>

    <h1 class="title">Total and Complete<br>Surrender for Total and<br>Complete Deliverance!</h1>

    <p class="summary">A prayer, anointing, and deliverance all night prayer service, at Brookhaven Assembly.</p>

    <div class="date-badge">
      <span class="date-day">Saturday</span>
      <span class="date-full">December 28 2013</span>
      <span class="date-time">from 9pm-6am.</span>
      <span class="date-program">Special guest speakers,<br>prayer, anointing,<br>and deliverance<br>sessions.</span>
    </div>

    <p class="contact">For more information contact Sis Mirela Thornbury at Brookhaven Assembly 347 562 1094 Ext. 4816 or Janelle Corbin at 631 538-2904</p>
  </main>
</body>
</html>
```